依頼詳細
不動産の案内所や現地、宣伝用に置けるような「のぼり旗」を作成したいと思います。
観光スポットなどをドライブしながらでも違和感のない感じだとありがたいです。
目には止まって欲しいけどリゾート地に設置したいのでカチカチなデザインでない方が良いです。
記載項目
碧浜ソレイユ、ロゴ、0995−61−2348、
※海が見える売土地あります

※この部分は変えられるようにしたいです。
・海が見える売物件
・管理地
・不動産案内所
・売地募集中
・不動産のことならお気軽にどうぞ
希望イメージ
シンプル 複雑
単色 カラフル
暗い 明るい
日常 高級
遊び心 厳粛
未来的 伝統的
女性的 男性的
希望する色
青系、水色系
納品ファイル
• イラストレーター形式 (.ai)
補足説明
その他、掲載した方が良い文字や表現などありましたら追加していただいて大丈夫です。
サイズを掲載するのを忘れましたが標準の横600×縦1800mmで考えております。
中身の文字は臨機応変に変更しようかと思っております。
よろしくお願いいたします。
■ 選んだ理由

リゾート地に設置した際にイメージに合いながらも目を引きそうな感じがとても気に入りました。

■ 提案者全員のお礼・コメント

とても素敵なデザインありがとうございました!!
貴重なお時間をかけて考えていただき感謝いたします。
また機会がありましたらぜひよろしくお願いいたします。

```html
<!DOCTYPE html>
<html lang="ja">
<head>
<meta charset="utf-8">
<title>海が見える売土地あります｜碧浜ソレイユ</title>
<link href="https://fonts.googleapis.com/css2?family=M+PLUS+1p:wght@500;700;800;900&display=swap" rel="stylesheet">
<style>
  :root {
    --paper: #ffffff;
    --brand-blue: #1a56b8;
    --outline-blue: #1650b0;
    --headline-yellow: #ffe21a;
    --headline-pale: #fff7b0;
    --phone-green: #62b22f;
    --ink: #1d2a48;
  }
  html, body {
    margin: 0;
    padding: 0;
    width: 1200px;
    height: 3608px;
    overflow: hidden;
    background: var(--paper);
  }
  p, h1 { margin: 0; }
  .banner {
    position: relative;
    width: 1200px;
    height: 3608px;
    overflow: hidden;
    font-family: "M PLUS 1p", sans-serif;
  }
  .backdrop {
    position: absolute;
    inset: 0;
    width: 1200px;
    height: 3608px;
  }
  .headline {
    position: absolute;
    writing-mode: vertical-rl;
    font-weight: 900;
    line-height: 1;
    paint-order: stroke fill;
  }
  .headline--sea {
    left: 585px;
    top: 110px;
    font-size: 520px;
    letter-spacing: -10px;
    color: var(--headline-yellow);
    background: linear-gradient(90deg, var(--headline-yellow) 0%, var(--headline-yellow) 55%, var(--headline-pale) 100%);
    -webkit-background-clip: text;
    background-clip: text;
    -webkit-text-fill-color: transparent;
    -webkit-text-stroke: 28px var(--outline-blue);
    filter: drop-shadow(10px 0 0 var(--paper)) drop-shadow(-10px 0 0 var(--paper)) drop-shadow(0 10px 0 var(--paper)) drop-shadow(0 -10px 0 var(--paper));
  }
  .headline--land {
    left: 100px;
    top: 140px;
    font-size: 340px;
    letter-spacing: 6px;
    color: var(--paper);
    -webkit-text-stroke: 24px var(--outline-blue);
  }
  .brand-mark {
    position: absolute;
    left: 0;
    top: 2880px;
    width: 1200px;
    display: flex;
    justify-content: center;
    align-items: center;
    gap: 28px;
    font-size: 86px;
    font-weight: 800;
    line-height: 1.2;
    color: var(--brand-blue);
  }
  .brand-mark__dot {
    width: 64px;
    height: 64px;
    border-radius: 50%;
    background: var(--brand-blue);
  }
  .company {
    position: absolute;
    left: 0;
    top: 3190px;
    width: 1200px;
    text-align: center;
    font-size: 58px;
    font-weight: 700;
    line-height: 1.2;
    color: var(--brand-blue);
    letter-spacing: 2px;
  }
  .phone {
    position: absolute;
    left: 0;
    top: 3290px;
    width: 1200px;
    display: flex;
    justify-content: center;
    align-items: center;
    gap: 22px;
    color: var(--phone-green);
    font-size: 116px;
    font-weight: 800;
    line-height: 1.1;
  }
  .phone__icon { width: 96px; height: 96px; }
  .address {
    position: absolute;
    left: 0;
    top: 3470px;
    width: 1200px;
    text-align: center;
    font-size: 46px;
    font-weight: 500;
    line-height: 1.2;
    color: var(--ink);
  }
</style>
</head>
<body>
<main class="banner">
  <svg class="backdrop" viewBox="0 0 1200 3608" role="img" aria-label="水彩風の青空と海、砂浜の風景">
    <defs>
      <linearGradient id="scene" x1="0" y1="0" x2="0" y2="1">
        <stop offset="0" stop-color="#9fd0f0"/>
        <stop offset="0.12" stop-color="#e6f3fb"/>
        <stop offset="0.22" stop-color="#a9d3ef"/>
        <stop offset="0.26" stop-color="#3e8fd3"/>
        <stop offset="0.36" stop-color="#1f6fc0"/>
        <stop offset="0.45" stop-color="#5aa8de"/>
        <stop offset="0.5" stop-color="#d8ecf4"/>
        <stop offset="0.58" stop-color="#ecd9b4"/>
        <stop offset="0.68" stop-color="#f3e6cc"/>
        <stop offset="0.76" stop-color="#ffffff"/>
        <stop offset="1" stop-color="#ffffff"/>
      </linearGradient>
    </defs>
    <rect width="1200" height="3608" fill="url(#scene)"/>
  </svg>

  <h1 class="headline headline--sea">海が見える</h1>
  <p class="headline headline--land">売土地あります</p>

  <div class="brand-mark"><span class="brand-mark__dot"></span>碧浜ソレイユ</div>

  <p class="company">碧浜ソレイユ株式会社</p>

  <p class="phone">
    <svg class="phone__icon" viewBox="0 0 100 100" aria-hidden="true">
      <path fill="currentColor" d="M50 18c-22 0-40 7-44 18l-2 10c0 3 3 5 6 4l16-4c3-1 4-3 4-6v-7c6-2 13-3 20-3s14 1 20 3v7c0 3 1 5 4 6l16 4c3 1 6-1 6-4l-2-10c-4-11-22-18-44-18z"/>
      <path fill="currentColor" d="M30 52l8-8h24l8 8 10 30H20z"/>
      <circle cx="50" cy="66" r="9" fill="#ffffff"/>
    </svg>
    <span>0995-61-2348</span>
  </p>

  <p class="address">〒904-0218 沖縄県浜風市字潮見台218</p>
</main>
</body>
</html>
```